Teach English in China Website Redesign Needed

We recruit native English speakers from the US, UK, etc. who want to teach English as a foreign language in schools in China. Our target customer is college educated, age 22-28 and they love to travel. We prefer designs with bright colors and lots of photos. We want to keep all the text on our current homepage, LanternClassroomHub.com. We are open to changing our logo. A competitor's page that we like is bluepeakmentors.com because of their bright colors, photos and use of white space. We are happy to give you a dofollow link and design credit on our homepage. The use of included photos is optional. We need at least a home page design and a standard blog post design.
Target Market(s)
Our target customer is college educated, age 22-28 and they love to travel. Half of our customers are kindergarten teachers. Half of our customers are male.
Logo Text
Lantern Classroom Hub
Number of Pages Required
2 page
Requirements
Must have
- Bright colors
Should not have
- Our homepage must not look crowded. Use white space effectively.

```html
<!DOCTYPE html>
<html lang="en">
<head>
<meta charset="utf-8">
<title>Lantern Classroom Hub – Why Choose Us</title>
<link href="https://fonts.googleapis.com/css2?family=Rajdhani:wght@500;600&family=Montserrat:wght@800&display=swap" rel="stylesheet">
<style>
  :root {
    --night: #0d1030;
    --lantern-red: #7a1410;
    --headline-yellow: #fff36b;
    --cream: #fffaa5;
    --leaf-green: #5a8a1a;
    --body-grey: #6a6a5a;
    --ink: #111111;
    --bullet-orange: #f05a14;
    --white: #ffffff;
  }
  * { margin: 0; padding: 0; box-sizing: border-box; }
  html, body { width: 1098px; height: 1200px; overflow: hidden; }
  body { font-family: "Rajdhani", sans-serif; font-weight: 500; background: var(--cream); position: relative; }

  .why-us {
    position: absolute; left: 0; top: 0; width: 1098px; height: 537px;
    background:
      radial-gradient(ellipse at 60% 10%, rgba(200,40,20,.55), transparent 45%),
      radial-gradient(ellipse at 90% 20%, rgba(180,30,20,.5), transparent 40%),
      linear-gradient(180deg, var(--night) 0%, #2a1530 45%, var(--lantern-red) 80%, #5a0e0c 100%);
  }
  .why-us__title {
    position: absolute; left: 81px; top: 60px;
    font-family: "Montserrat", sans-serif; font-weight: 800; font-size: 33px;
    color: var(--headline-yellow); letter-spacing: .5px;
  }
  .why-us__list { position: absolute; left: 81px; top: 129px; width: 530px; list-style: none; }
  .why-us__list li {
    position: relative; padding-left: 24px; color: var(--white);
    font-size: 14.2px; line-height: 21px; margin-bottom: 11.5px; font-weight: 600;
  }

  .bullet { position: absolute; left: 0; top: 5px; width: 11px; height: 11px; }

  .video-still {
    position: absolute; left: 623px; top: 130px; width: 394px; height: 264px;
    background: radial-gradient(ellipse at 60% 45%, #6a6a80, #2a2a3a 70%, #15151f);
  }
  .video-still__play { position: absolute; left: 798px; top: 240px; }

  .job {
    position: absolute; left: 0; top: 537px; width: 1098px; height: 663px; background: var(--cream);
  }
  .job__title {
    position: absolute; left: 0; top: 56px; width: 100%; text-align: center;
    font-family: "Montserrat", sans-serif; font-weight: 800; font-size: 32px; color: var(--leaf-green);
  }
  .job__intro {
    position: absolute; left: 80px; top: 117px; width: 938px;
    text-align: justify; text-align-last: center;
    font-size: 13.6px; line-height: 21px; color: var(--body-grey);
  }
  .job__note {
    position: absolute; left: 0; top: 204px; width: 100%; text-align: center;
    font-size: 13.5px; color: var(--ink);
  }
  .job__col { position: absolute; top: 276px; }
  .job__col--required { left: 81px; width: 400px; }
  .job__col--offer { left: 529px; width: 482px; }
  .job__col h3 { font-size: 14px; font-weight: 600; color: var(--ink); margin-bottom: 10px; }
  .job__col ul { list-style: none; }
  .job__col li {
    position: relative; padding-left: 19px; font-size: 13px; line-height: 19.5px;
    color: var(--body-grey); margin-bottom: 9.7px;
  }
  .job__col li .bullet { top: 4px; }
</style>
</head>
<body>
<svg width="0" height="0" style="position:absolute">
  <defs>
    <symbol id="arrow-bullet" viewBox="0 0 12 12">
      <circle cx="6" cy="6" r="6" fill="#f05a14"/>
      <path d="M3 6h5M6 3.5L8.5 6 6 8.5" stroke="#fff" stroke-width="1.6" fill="none" stroke-linecap="round" stroke-linejoin="round"/>
    </symbol>
  </defs>
</svg>

<section class="why-us" role="img" aria-label="Night view of a Chinese temple decorated with rows of red lanterns">
  <h2 class="why-us__title">WHY CHOOSE US</h2>
  <ul class="why-us__list">
    <li><svg class="bullet"><use href="#arrow-bullet"/></svg>Competitive compensation: 7000-9000 RMB/month, up to 18,000 RMB (divide by 6.5<br>for&nbsp; US dollars) if you have a bachelor’s degree, 2+ years of teaching experience</li>
    <li><svg class="bullet"><use href="#arrow-bullet"/></svg>Housing allowance: 2000 RMB/month (housing is cheaper in China)</li>
    <li><svg class="bullet"><use href="#arrow-bullet"/></svg>Teach private English lessons after work for 250 RMB/hr ($38 US per hour)</li>
    <li><svg class="bullet"><use href="#arrow-bullet"/></svg>Airfare reimbursement: 5000 RMB at end of completed 1 year contract</li>
    <li><svg class="bullet"><use href="#arrow-bullet"/></svg>Free TESOL / TEFL training and certification</li>
    <li><svg class="bullet"><use href="#arrow-bullet"/></svg>Invitation letter so you can apply for a visa (Z visa if you have a bachelor’s degree).</li>
    <li><svg class="bullet"><use href="#arrow-bullet"/></svg>Airport pickup</li>
    <li><svg class="bullet"><use href="#arrow-bullet"/></svg>5-day work week, 25 hours teaching per week plus some office hours</li>
    <li><svg class="bullet"><use href="#arrow-bullet"/></svg>20 paid holidays</li>
    <li><svg class="bullet"><use href="#arrow-bullet"/></svg>Free Chinese classes 2 hours per week with most jobs</li>
  </ul>
</section>

<div class="video-still" role="img" aria-label="Video still of a teacher hugging a group of young students"></div>
<svg class="video-still__play" width="44" height="44" viewBox="0 0 44 44" aria-hidden="true">
  <circle cx="22" cy="22" r="21" fill="rgba(255,255,255,.25)" stroke="#ffffff" stroke-width="2"/>
  <path d="M17 13l13 9-13 9z" fill="#ffffff"/>
</svg>

<section class="job">
  <h2 class="job__title">JOB DESCRIPTION</h2>
  <p class="job__intro">We are seeking English speakers from the US, UK, Canada, Ireland, Australia, New Zealand and South Africa to teach English in China for a year.&nbsp; A Bachelor’s degree and expe&shy;rience is recommended, but if you want to work in a kindergarten, you can teach English in China without a degree. If you have a Bachelor’s degree, you also have the option to teach older children and adults. Also, more good news is that you do NOT need to know how to speak Chinese.</p>
  <p class="job__note">General Job Requirements (See our current job openings for details on all jobs.)</p>

  <div class="job__col job__col--required">
    <h3>Required:</h3>
    <ul>
      <li><svg class="bullet"><use href="#arrow-bullet"/></svg>Must be at least 18 years old</li>
      <li><svg class="bullet"><use href="#arrow-bullet"/></svg>High School Diploma or equivalent</li>
      <li><svg class="bullet"><use href="#arrow-bullet"/></svg>Speak, read, and write English fluently</li>
      <li><svg class="bullet"><use href="#arrow-bullet"/></svg>Hands-on teaching experience preferred but not required</li>
      <li><svg class="bullet"><use href="#arrow-bullet"/></svg>Excellent verbal communication skills</li>
      <li><svg class="bullet"><use href="#arrow-bullet"/></svg>High level of flexibility</li>
    </ul>
  </div>

  <div class="job__col job__col--offer">
    <h3>We Offer :</h3>
    <ul>
      <li><svg class="bullet"><use href="#arrow-bullet"/></svg>Competitive compensation: 8000-18,000 RMB/month, up to 40,000 RMB per month if<br>You have a teaching license to teach in your country’s public schools</li>
      <li><svg class="bullet"><use href="#arrow-bullet"/></svg>Housing allowance: 2000-4000 RMB/month (housing is cheaper in most of China)</li>
      <li><svg class="bullet"><use href="#arrow-bullet"/></svg>Airfare reimbursement: 6000 RMB at end of completed 1-year contract</li>
      <li><svg class="bullet"><use href="#arrow-bullet"/></svg>Free TESOL / TEFL training and certification through TutorVoyage.com</li>
      <li><svg class="bullet"><use href="#arrow-bullet"/></svg>Invitation letter so you can apply for a visa (Z visa if you have a bachelor’s degree).</li>
      <li><svg class="bullet"><use href="#arrow-bullet"/></svg>Airport pickup</li>
      <li><svg class="bullet"><use href="#arrow-bullet"/></svg>5-day work week, 25 hours teaching per week plus some office hours</li>
      <li><svg class="bullet"><use href="#arrow-bullet"/></svg>20 paid holidays</li>
      <li><svg class="bullet"><use href="#arrow-bullet"/></svg>Free Chinese classes 2 hours per week with most jobs</li>
    </ul>
  </div>
</section>
</body>
</html>
```